KVT Business Cards

We require business cards for our business. We would like a matte black back to the card, with our logo centred in the middle. The front side of the card is open to design.

Target Market(s)

Clients looking for legal services (professional)

Industry/Entity Type

Legal

Contact Information for Business Card

Boris Telemark
Partner
Mobile: 0438 715 642
Email: boris@kvtlaw.co
Website: www.kvtlaw.co
Level 3, 118 Wexbury Street
Sydney NSW 2000

Font styles to use
Other font styles liked:
• Avenir

Colors
f04a50
ffffff
1b1b1b

Requirements
Must have
• Black back with logo included in the centre of the card.
• Our font is Avenir.

```html
<!DOCTYPE html>
<html lang="en">
<head>
<meta charset="UTF-8">
<title>KVT Business Cards</title>
<link href="https://fonts.googleapis.com/css2?family=Nunito+Sans:wght@400;600;700&display=swap" rel="stylesheet">
<style>
  :root {
    --brand-red: #f04a50;
    --brand-white: #ffffff;
    --brand-black: #1b1b1b;
    --stage: #2a2b2b;
    --ink: #161616;
  }
  * { margin: 0; padding: 0; box-sizing: border-box; }
  html, body { width: 1200px; height: 1200px; overflow: hidden; }
  body {
    background: var(--stage);
    font-family: "Nunito Sans", "Avenir", sans-serif;
    display: flex;
    flex-direction: column;
    align-items: center;
    justify-content: center;
    gap: 64px;
  }
  .card {
    position: relative;
    width: 760px;
    height: 464px;
    overflow: hidden;
    border-radius: 4px;
    box-shadow: 0 18px 40px rgba(0,0,0,0.45);
  }

  /* Front side */
  .card-front { background: var(--brand-red); }
  .front-band {
    position: absolute;
    left: 0; right: 0; bottom: 34px;
    height: 70px;
    background: var(--brand-black);
  }
  .front-band-rule {
    position: absolute;
    left: 0; right: 0; bottom: 22px;
    height: 6px;
    background: var(--brand-black);
  }
  .contact {
    position: absolute;
    right: 44px;
    top: 88px;
    text-align: right;
  }
  .contact-name {
    font-size: 40px;
    font-weight: 600;
    color: var(--ink);
    letter-spacing: 0.5px;
    line-height: 1.1;
  }
  .contact-title {
    font-size: 24px;
    font-weight: 600;
    color: var(--ink);
    margin-bottom: 18px;
  }
  .contact-line {
    font-size: 25px;
    font-weight: 600;
    color: var(--brand-white);
    line-height: 1.32;
  }

  /* Back side */
  .card-back {
    background: var(--brand-black);
    display: flex;
    align-items: center;
    justify-content: center;
  }
  .firm-mark {
    display: flex;
    align-items: center;
    gap: 22px;
  }
  .firm-square {
    width: 44px;
    height: 44px;
    background: var(--brand-red);
  }
  .firm-name {
    font-size: 38px;
    font-weight: 600;
    color: var(--brand-white);
    line-height: 1.05;
    letter-spacing: 1px;
    text-transform: uppercase;
  }
</style>
</head>
<body>

  <section class="card card-front" aria-label="Business card front">
    <div class="front-band"></div>
    <div class="front-band-rule"></div>
    <div class="contact">
      <p class="contact-name">Boris Telemark</p>
      <p class="contact-title">Partner</p>
      <p class="contact-line">Mobile: 0438 715 642</p>
      <p class="contact-line">Email: boris@kvtlaw.co</p>
      <p class="contact-line">Website: www.kvtlaw.co</p>
      <p class="contact-line">Level 3, 118 Wexbury Street</p>
      <p class="contact-line">Sydney NSW 2000</p>
    </div>
  </section>

  <section class="card card-back" aria-label="Business card back">
    <div class="firm-mark">
      <span class="firm-square"></span>
      <p class="firm-name">Kovar Vance<br>Telemark Legal</p>
    </div>
  </section>

</body>
</html>
```